Lorna Tess Tresses Fancy Business Card’s

I want my business cards to be elite, original and very classy. I want the business cards to match the colors of my logo and to match the design posted. I would love the design of the picture I posted

I want the card all white .
The dripping on the top of the card I want it to match the pink color in my logo that’s also posted .
I need my logo on the business card !
I need my Instagram- @lorna.tess.tresses__
And my phone number - 582 907 3365

Target Market(s)

My target market is young woman age 23 to older woman to the age of 65
I want both older and younger women to love my design . I don’t want any cheap looking business cards

Industry/Entity Type

Hair And Beauty

Contact Information for Business Card

Add my logo
Add my Instagram- @lorna.tess.tresses__
My number - 582 907 3365
My website- www.lornatesstresses.example

Font styles to use
Serif
Script

Colors
ffffff
e667a6
e34298

Requirements
Must have
• The business cards must have my logo, my number , my website, and my Instagram!
Nice to have
• Nice to have glitter words that match my logo
• The business cards must look classy and mature
• I want them to be very unique!!
Should not have
• Should not have any colors that doesn’t match my logo ! This is very important! Please

```html
<!DOCTYPE html>
<html lang="en">
<head>
<meta charset="utf-8">
<title>Lorna Tess Tresses – Business Cards</title>
<link rel="stylesheet" href="https://fonts.googleapis.com/css2?family=Playfair+Display:wght@600&family=Montserrat:wght@400&display=swap">
<style>
  :root {
    --backdrop: #1e1e1e;
    --card-white: #ffffff;
    --brand-pink: #e34298;
    --soft-pink: #e667a6;
    --ink: #3a3a3a;
  }
  * { box-sizing: border-box; margin: 0; padding: 0; }
  html, body {
    width: 1200px;
    height: 1021px;
    overflow: hidden;
    background: var(--backdrop);
  }
  .canvas {
    position: relative;
    width: 1200px;
    height: 1021px;
  }
  .card {
    position: absolute;
    left: 260px;
    width: 680px;
    height: 388px;
    background: var(--card-white);
    border: 14px solid var(--brand-pink);
  }
  .card--front { top: 110px; }
  .card--back { top: 530px; }

  .brand-name {
    font-family: "Playfair Display", Georgia, serif;
    font-weight: 600;
    color: var(--brand-pink);
    line-height: 1.05;
  }
  .card--front .brand-name {
    position: absolute;
    inset: 0;
    display: flex;
    align-items: center;
    justify-content: center;
    font-size: 50px;
    letter-spacing: 0.5px;
  }
  .card--back .brand-name {
    position: absolute;
    left: 48px;
    top: 118px;
    width: 250px;
    font-size: 42px;
  }
  .contact-list {
    position: absolute;
    left: 318px;
    top: 136px;
    list-style: none;
    font-family: "Montserrat", Arial, sans-serif;
    font-size: 19px;
    color: var(--ink);
  }
  .contact-item {
    display: flex;
    align-items: center;
    gap: 12px;
    margin-bottom: 10px;
    white-space: nowrap;
  }
  .contact-icon {
    width: 20px;
    height: 20px;
    flex: none;
  }
</style>
</head>
<body>
<main class="canvas">
  <section class="card card--front" aria-label="Business card front">
    <p class="brand-name">Lorna Tess Tresses</p>
  </section>

  <section class="card card--back" aria-label="Business card back">
    <p class="brand-name">Lorna Tess<br>Tresses</p>
    <ul class="contact-list">
      <li class="contact-item">
        <svg class="contact-icon" viewBox="0 0 20 20" aria-hidden="true">
          <rect x="3" y="3" width="14" height="14" fill="none" stroke="#e34298" stroke-width="2"/>
        </svg>
        <span>@lorna.tess.tresses__</span>
      </li>
      <li class="contact-item">
        <svg class="contact-icon" viewBox="0 0 24 24" aria-hidden="true">
          <path fill="#e34298" d="M6.6 10.8a15.1 15.1 0 0 0 6.6 6.6l2.2-2.2c.3-.3.7-.4 1-.2 1.1.4 2.3.6 3.6.6.6 0 1 .4 1 1V20c0 .6-.4 1-1 1A17 17 0 0 1 3 4c0-.6.4-1 1-1h3.5c.6 0 1 .4 1 1 0 1.3.2 2.5.6 3.6.1.3 0 .7-.2 1z"/>
        </svg>
        <span>582 907 3365</span>
      </li>
      <li class="contact-item">
        <svg class="contact-icon" viewBox="0 0 20 20" aria-hidden="true">
          <g fill="none" stroke="#e34298" stroke-width="1.5">
            <circle cx="10" cy="10" r="8"/>
            <ellipse cx="10" cy="10" rx="3.5" ry="8"/>
            <line x1="2" y1="10" x2="18" y2="10"/>
            <line x1="3.5" y1="6" x2="16.5" y2="6"/>
            <line x1="3.5" y1="14" x2="16.5" y2="14"/>
          </g>
        </svg>
        <span>www.lornatesstresses.example</span>
      </li>
    </ul>
  </section>
</main>
</body>
</html>
```